Price Trend Graphic for Estimates

I want to add a graphic to my estimates that shows the projected price trend of the work we are quoting to the customer. I have attached a couple ideas I was working on but they are garbage. Hopefully you can see the intent and make it look a lot better. Basically I want the customer to see a really a professional / technological graphic that will stimulate them to purchase Right Now! before the price goes up further. So maybe if the "Today's Price" looks nice and friendly and then becomes more critical and ominous as it goes forward 30 days.... 90 days.... Idea is to psychologically

Target Market(s)

Customers for our Construction business

Industry/Entity Type

Construction

Colors
0054AA
0677BA
7BADD7
CADEEF
E8F1F8
0094D4
00A9DD
6FCCEA
C7EBF8
E9F6FB
FFF300
FFF600
FEFA6F
FFFEC7
FFFEE8
F0912C
F2A743
F7CA91
FBE8D2
FDF5EE

Requirements
Must have
• nice looking graphic with upwards moving arrow and 3 price points
Nice to have
• technological / modern looking chart

```html
<!DOCTYPE html>
<html lang="en">
<head>
<meta charset="utf-8">
<title>Estimated Price Trend</title>
<link rel="stylesheet" href="https://fonts.googleapis.com/css2?family=Oswald:wght@500&family=Poppins:wght@300;400;600;800&display=swap">
<style>
  :root{
    --page:#ffffff;
    --navy-top:#141838;
    --navy-mid:#0c2560;
    --blue-bottom:#0a3aa8;
    --grid:rgba(90,130,220,0.16);
    --orange:#ff5a14;
    --orange-soft:#f7931e;
    --teal:#1fd6c6;
    --sky:#15b8ec;
    --sky-text:#27c3ee;
    --aqua-text:#40e3d5;
    --ring:#0d1c44;
    --white:#ffffff;
    --title-light:#d9dce3;
  }
  html,body{margin:0;width:1200px;height:1200px;overflow:hidden;background:var(--page);}
  .price-trend{
    position:absolute;left:73px;top:193px;width:1053px;height:813px;
    box-shadow:0 6px 30px rgba(0,0,0,0.35);
  }
  .price-trend svg{display:block;width:100%;height:100%;}
  .price-figure{font-family:"Oswald",sans-serif;font-weight:500;}
  .price-label{font-family:"Poppins",sans-serif;font-weight:600;fill:var(--white);letter-spacing:0.5px;}
  .legend-text{font-family:"Oswald",sans-serif;font-weight:500;fill:var(--white);font-size:27px;}
  .title-accent{font-family:"Poppins",sans-serif;font-weight:800;fill:var(--teal);}
  .title-light{font-family:"Poppins",sans-serif;font-weight:300;fill:var(--title-light);}
  .title-bold{font-family:"Poppins",sans-serif;font-weight:800;fill:var(--title-light);}
</style>
</head>
<body>
<div class="price-trend">
<svg viewBox="91 241 1317 1017" preserveAspectRatio="none" xmlns="http://www.w3.org/2000/svg">
  <defs>
    <linearGradient id="bg" x1="0" y1="0" x2="0" y2="1">
      <stop offset="0" stop-color="var(--navy-top)"/>
      <stop offset="0.55" stop-color="var(--navy-mid)"/>
      <stop offset="1" stop-color="var(--blue-bottom)"/>
    </linearGradient>
    <linearGradient id="area" x1="0" y1="0" x2="1" y2="0">
      <stop offset="0" stop-color="#0a45b0" stop-opacity="0.25"/>
      <stop offset="0.6" stop-color="#0b7cb8" stop-opacity="0.55"/>
      <stop offset="1" stop-color="#12a894" stop-opacity="0.8"/>
    </linearGradient>
    <filter id="glow" x="-20%" y="-20%" width="140%" height="140%">
      <feGaussianBlur stdDeviation="6" result="b"/>
      <feMerge><feMergeNode in="b"/><feMergeNode in="SourceGraphic"/></feMerge>
    </filter>
  </defs>

  <rect class="backdrop" x="91" y="241" width="1317" height="1017" fill="url(#bg)"/>

  <g class="grid" stroke="var(--grid)" stroke-width="1">
    <path d="M91 540H1408M91 610H1408M91 680H1408M91 750H1408M91 820H1408M91 890H1408M91 960H1408"/>
    <path d="M200 300V1000M330 300V1000M460 300V1000M590 300V1000M720 300V1000M850 300V1000M980 300V1000M1110 300V1000M1240 300V1000M1370 300V1000"/>
  </g>

  <path class="trend-area" d="M91 1197L341 987L537 1050L672 887L898 848L1175 623L1408 553V1258H91Z" fill="url(#area)"/>

  <polyline class="trend-line" points="91,1197 341,987 537,1050 672,887 898,848 1175,623 1408,553"
    fill="none" stroke="var(--white)" stroke-width="4" filter="url(#glow)"/>

  <g class="trend-arrow" filter="url(#glow)">
    <polyline points="91,1145 343,930 537,1000 672,835 898,797 1170,570"
      fill="none" stroke="var(--orange)" stroke-width="7" stroke-linejoin="round"/>
    <polygon points="1212,522 1152,545 1195,583" fill="var(--orange)"/>
  </g>

  <g class="markers" stroke="var(--white)" stroke-width="4">
    <circle cx="341" cy="987" r="15" fill="var(--teal)"/>
    <circle cx="898" cy="848" r="15" fill="var(--sky)"/>
    <circle cx="1175" cy="623" r="15" fill="var(--orange-soft)"/>
  </g>

  <g class="donut" transform="translate(273 420)">
    <circle r="74" fill="var(--ring)" stroke="#1b3d8a" stroke-width="3" filter="url(#glow)"/>
    <circle r="46" fill="none" stroke="var(--orange-soft)" stroke-width="46" pathLength="100" stroke-dasharray="30 70" transform="rotate(-90)"/>
    <circle r="30" fill="var(--white)" stroke="#9aa3b5" stroke-width="5"/>
  </g>
  <g class="donut" transform="translate(461 420)">
    <circle r="74" fill="var(--ring)" stroke="#1b3d8a" stroke-width="3" filter="url(#glow)"/>
    <circle r="46" fill="none" stroke="var(--teal)" stroke-width="46" pathLength="100" stroke-dasharray="64 36" transform="rotate(-90)"/>
    <circle r="30" fill="var(--white)" stroke="#a8e8e2" stroke-width="5"/>
  </g>
  <g class="donut" transform="translate(651 420)">
    <circle r="74" fill="var(--ring)" stroke="#1b3d8a" stroke-width="3" filter="url(#glow)"/>
    <circle r="46" fill="none" stroke="var(--sky)" stroke-width="46" pathLength="100" stroke-dasharray="90 10" transform="rotate(-90)"/>
    <circle r="30" fill="var(--white)" stroke="#a6def3" stroke-width="5"/>
  </g>

  <g class="legend">
    <circle cx="205" cy="528" r="8" fill="var(--orange-soft)"/>
    <text class="legend-text" x="223" y="538">$ 6,500.00</text>
    <circle cx="392" cy="528" r="8" fill="var(--teal)"/>
    <text class="legend-text" x="411" y="538">$7,280.00 30</text>
    <circle cx="599" cy="528" r="8" fill="var(--sky)"/>
    <text class="legend-text" x="619" y="538">$7,460.00 60</text>
  </g>

  <g class="price-point">
    <text class="price-figure" x="229" y="852" font-size="52" fill="var(--orange)">$ 6,500.00</text>
    <text class="price-label" x="231" y="887" font-size="27">TODAY PRICE</text>
  </g>
  <g class="price-point">
    <text class="price-figure" x="688" y="690" font-size="52" fill="var(--sky-text)">$7,280.00 30</text>
    <text class="price-label" x="689" y="726" font-size="27">30 DAYS PRICE</text>
  </g>
  <g class="price-point">
    <text class="price-figure" x="1057" y="462" font-size="52" fill="var(--aqua-text)">$7,460.00 60</text>
    <text class="price-label" x="1058" y="497" font-size="27">90 DAYS PRICE</text>
  </g>

  <g class="headline" text-anchor="end">
    <text class="title-accent" x="1352" y="1098" font-size="90">ESTIMATED</text>
    <text x="1352" y="1193" font-size="90"><tspan class="title-light">PRICE </tspan><tspan class="title-bold">TREND</tspan></text>
  </g>
</svg>
</div>
</body>
</html>
```